Web Design Project: Facility Management company

Hi! We need a new website.

Our current website: http://www.vireo-trade.ru/ and we don-t like it. =)
The structure of our company has changed and now we don't need "cleaning" and "engeneering" on this site.

We are facility management company in Russia. So we provide integrated service solutions specific to industrial services: maintenance, repair, etc. of engineering systems.
More services:
Energy planning
Automation
Audit
Statements with regulators
Video surveillance
Central heating
Security systems
Welding
Management of subcontractors
Electrical installation and service needs
Reception
Catering

Visitors:
* Managers in the field of commercial real estate
* Chief engineers
* TOP managers of large companies, malls, factories...
+ their subordinates
* Small% of applicants.

Here you can see some websites/patterns we liked:
http://www.kobalmire.ru/ (This is our competitor’s site, so our site shouldn’t be an exact copy))))
http://www.dwatqo.ru/
http://www.layoutfarrow.com/demo/24296.html
http://www.layoutfarrow.com/website-templates/10145.html

Style:
Light, hi-tech/minimalizm, the color palette should be based on the original site colors (Green + black + white). http://www.vireo-trade.ru/

Estimated sitemap:
1. Home
2. About Us
3. Company's policy
4. History + Achievements.
5. Certificates
6. Map of presence (Here you can use sample map in file "our projects")
7. Services
8. Portfolio
9. News or blog
10. Jobs
11. Contacts - with the feedback form (or the function "call to order")
12. English

Need a design pages: main page, page 404. The rest of the page could be created by general pattern.

Logo, navigation bar and contacts should be visible on all pages of a site.
Flash animation elements and buttons, etc. - not needed.

* We need to develop 3 websites, so we are looking for a long term cooperation.
Looking forward to your creativity =)

Must Have:
Clear, intuitive structure of web pages.
In the center - of pictures reflecting our main services (industrial theme). May be in rotation.
BUT! This banner (central picture) should not be a huge one =)
All relevant information should be visible at once without scrolling.

A possibility to place media files (presentations, video ...) and 2 banner links on the main page.

Font should be available in Cyrillic.
Updates

IMPORTANT!

Please notice that in thisdesign we don't need "cleaning" and "engeneering" on this site.

So don't use old block of 4pictures from our current website. We don't need it anymore. 

Thestructure of our company has changed and now we need some links (may be banners,may be something else) to our future cleaning website as well as engeneeringwebsite.
It should look like seperate (partner) companies, not like our sevices.

Regards, Vera.

Please don't forget that we need bilingual site.

So define language changing tool in your designs.

Industry/Entity Type

Industrial

```html
<!DOCTYPE html>
<html lang="en">
<head>
<meta charset="utf-8">
<title>Vireo — Engineering Systems</title>
<link rel="stylesheet" href="https://fonts.googleapis.com/css2?family=Oswald:wght@300;400&family=Arimo:wght@400&display=swap">
<style>
:root{
  --green:#8aa636;
  --green-dark:#6e8c1c;
  --heading:#7f9a26;
  --page:#eceeea;
  --white:#ffffff;
  --frame:#d9dcd6;
  --text:#4a4a4a;
  --muted:#9a9a9a;
  --nav-text:#4d6b12;
}
*{box-sizing:border-box;margin:0;padding:0}
html,body{width:1200px;height:851px;overflow:hidden}
body{background:var(--page);font-family:"Arimo",Arial,sans-serif;position:relative}
.header{position:absolute;left:0;top:0;width:1200px;height:112px;background:var(--green)}
.brand{position:absolute;left:46px;top:40px;display:flex;align-items:center;gap:10px;color:var(--white);font-family:"Oswald",sans-serif;font-weight:400;font-size:32px;letter-spacing:1px}
.brand-mark{width:16px;height:16px;background:var(--white)}
.lang{position:absolute;left:1011px;top:0;width:143px;height:30px;background:var(--white);border-radius:0 0 6px 6px;display:flex;font-family:"Oswald",sans-serif;font-size:16px}
.lang a{flex:1;text-align:center;line-height:28px;color:var(--green-dark);text-decoration:none;letter-spacing:1px}
.lang a.active{background:#f0f2ea}
.phone{position:absolute;left:890px;top:52px;display:flex;align-items:center;gap:18px;color:var(--white);font-family:"Oswald",sans-serif;font-weight:300;font-size:28px;letter-spacing:1px}
.nav{position:absolute;left:0;top:117px;width:1200px;height:52px;background:var(--white);border-bottom:2px solid var(--frame)}
.nav ul{list-style:none;display:flex;position:absolute;left:16px;top:0;height:52px;align-items:center}
.nav li{font-family:"Oswald",sans-serif;font-size:16px;letter-spacing:.5px;color:var(--nav-text);padding:0 23px;border-left:1px solid #c9d3ad;line-height:16px}
.nav li:first-child{border-left:none}
.search{position:absolute;left:916px;top:11px;width:208px;height:32px;background:#e2e3e0;border:1px solid #cfd0cc;font-family:"Oswald",sans-serif;font-size:13px;color:#888;padding:7px 14px;letter-spacing:1px}
.search-icon{position:absolute;left:1122px;top:8px}
.hero{position:absolute;left:39px;top:178px;width:1117px;height:278px;background:var(--white);border:3px solid var(--frame)}
.hero-photo{position:absolute;left:0;top:0;width:606px;height:272px;background:linear-gradient(90deg,#8f9aa3 0%,#b9c0c5 45%,#c8ced2 80%,#ffffff 100%)}
.hero-title{position:absolute;right:54px;top:22px;text-align:right;font-family:"Oswald",sans-serif;font-weight:300;font-size:35px;line-height:42px;color:var(--heading);letter-spacing:1.5px}
.hero-text{position:absolute;left:637px;top:130px;width:423px;font-family:"Oswald",sans-serif;font-weight:300;font-size:14.5px;line-height:27px;color:var(--muted);text-transform:uppercase;letter-spacing:1px;text-align:justify}
.intro{position:absolute;left:40px;top:472px;width:766px;color:var(--text)}
.intro h1{font-family:"Oswald",sans-serif;font-weight:300;font-size:22px;color:var(--heading);letter-spacing:.8px;margin-bottom:24px}
.intro ul{list-style:none;font-size:14px;line-height:20.5px;margin-bottom:20px}
.intro li{padding-left:16px;position:relative}
.intro li::before{content:"";position:absolute;left:2px;top:6px;border-left:5px solid #666;border-top:4px solid transparent;border-bottom:4px solid transparent}
.intro p{font-size:14px;line-height:20.5px;text-align:justify;margin-bottom:20px}
.intro a{color:#111}
.tabs{position:absolute;left:853px;top:481px;display:flex;gap:12px}
.tab{width:90px;height:30px;font-size:16px;text-align:center;line-height:28px;border:2px solid var(--frame);border-bottom:none;background:var(--white);color:#555}
.tab.active{background:var(--green);color:var(--white);border-color:var(--white)}
.news{position:absolute;left:836px;top:511px;width:320px;height:246px;background:var(--white);border:3px solid var(--frame);padding:14px 10px 0 37px}
.news-item{position:relative;font-size:14px;line-height:20.5px;color:var(--muted);text-align:justify;height:61.5px;overflow:hidden;margin-bottom:15px}
.news-item::before{content:"";position:absolute;left:-24px;top:6px;border-left:5px solid #bbb;border-top:4px solid transparent;border-bottom:4px solid transparent}
.news-sep{position:absolute;left:873px;width:268px;height:1px;background:#e6e6e6}
.footer{position:absolute;left:0;top:771px;width:1200px;height:73px;background:var(--green);color:var(--white);font-size:14px;text-align:center}
.footer-links{padding-top:14px}
.footer-links span{margin:0 10px}
.footer-copy{margin-top:8px}
</style>
</head>
<body>
<header class="header">
  <div class="brand"><span class="brand-mark"></span>VIREO</div>
  <nav class="lang"><a href="#">RUS</a><a href="#" class="active">ENG</a></nav>
  <div class="phone">
    <svg width="26" height="36" viewBox="0 0 26 36" aria-hidden="true">
      <rect x="1" y="1" width="24" height="34" rx="3" fill="#fff"/>
      <rect x="5" y="5" width="16" height="9" fill="#8aa636"/>
      <g fill="#8aa636"><rect x="5" y="18" width="4" height="3"/><rect x="11" y="18" width="4" height="3"/><rect x="17" y="18" width="4" height="3"/><rect x="5" y="24" width="4" height="3"/><rect x="11" y="24" width="4" height="3"/><rect x="17" y="24" width="4" height="3"/></g>
    </svg>
    +7 812 555 0142
  </div>
</header>
<nav class="nav">
  <ul><li>HOME</li><li>ABOUT US</li><li>HISTORY</li><li>SERVICES</li><li>PORTFOLIO</li><li>JOBS</li><li>CONTACT US</li></ul>
  <div class="search">SEARCH...</div>
  <svg class="search-icon" width="36" height="36" viewBox="0 0 36 36" aria-hidden="true">
    <circle cx="21" cy="14" r="10" fill="none" stroke="#111" stroke-width="3.5"/>
    <line x1="14" y1="21" x2="4" y2="31" stroke="#111" stroke-width="5" stroke-linecap="round"/>
  </svg>
</nav>
<section class="hero">
  <div class="hero-photo" role="img" aria-label="Photo of an industrial pump room with steel tanks and a blue pump"></div>
  <h2 class="hero-title">INTEGRATED FACILITY<br>MANAGEMENT</h2>
  <p class="hero-text">Lorem ipsum dolor sit amet, consectetur adipiscing elit. Donec adipiscing dolor a magna consequat dapibus. Praesent non ante id nisi aliquam placerat. Phasellus porta vulputate bibendum.</p>
</section>
<section class="intro">
  <h1>WELCOME TO VIREO ENGINEERING SYSTEMS</h1>
  <ul>
    <li>Commercial property management</li>
    <li>Complex maintenance of immovable property</li>
    <li>Commercial property maintenance service</li>
  </ul>
  <p>These are the most important aspects of acquisition of the highest possible incomes from the commercial property object`s operation regardless of their purpose: it can be production, business center, a building of a shop, bank, restaurant, warehousing logistic complex, hotel or the biggest shopping and recreation center.</p>
  <p>More and more modern companies – proprietors and developer companies, hand over maintenance of the buildings, structures with all installation for outsourcing to a professional management company. <a href="#">More...</a></p>
</section>
<div class="tabs"><div class="tab active">NEWS</div><div class="tab">BLOG</div></div>
<aside class="news">
  <p class="news-item">Lorem ipsum dolor sit amet, consectetur adipiscing elit. Donec adipiscing dolor a magna consequat dapibus. Praesent non</p>
  <p class="news-item">Lorem ipsum dolor sit amet, consectetur adipiscing elit. Donec adipiscing dolor a magna consequat dapibus. Praesent non</p>
  <p class="news-item">Lorem ipsum dolor sit amet, consectetur adipiscing elit. Donec adipiscing dolor a magna consequat dapibus. Praesent non</p>
</aside>
<div class="news-sep" style="top:592px"></div>
<div class="news-sep" style="top:669px"></div>
<footer class="footer">
  <div class="footer-links">Company<span>|</span>Chosen by<span>|</span>Contact us<span>|</span>Integrated facility management<span>|</span>Technical maintenance of engineering systems<span>|</span>Company policy</div>
  <div class="footer-copy">All rights reserved @ vireo-trade.ru</div>
</footer>
</body>
</html>
```